User-interface and web design for new forum-style communication platform

We developed a new forum-style communication platform specially targetting stock investors to share and discuss information on companies listed on the stock exchange.

You have complete freedom for designing the user-interface and web design. Designs should include all features listed below.

Please read the attached document for full specifications. Also attached is a mockup of the layout, but this is only directional. A mockup for the user-profile is also attached, but does not need to be designed.

This project focusses on the homepage and thread view.

The winner(s) will be asked to design the complete project. (create thread box, user profile, registering, settings...)

We are looking for a well thought out, smart design that incorporates the specifications in the attached document. Please do not hesitate to contact us if anything is not clear.

Target Market(s)

Stock investors from 25 to 60 years old (the people that are currently on investor forums)

Industry/Entity Type

Communication

Font styles to use
Sans Serif

Colors

Designer to choose colors to be used in the design.

Requirements
Must have
• Full homepage design & Thread view specified in the attached document.
Nice to have
• Create thread view
- Field for adding tags
- field for subject of the thread
- text box with basic text editing
- method for sharing media
Should not have
• Logo design.

```html
<!DOCTYPE html>
<html lang="en">
<head>
<meta charset="utf-8">
<title>Conversations – Public #norvale#brightcap</title>
<link rel="stylesheet" href="https://fonts.googleapis.com/css2?family=Open+Sans:wght@400;600&family=PT+Sans+Narrow:wght@700&display=swap">
<style>
:root{
  --page-bg:#ececec;
  --header-bg:#f2f2f2;
  --footer-bg:#c4c4c4;
  --panel-bg:#ffffff;
  --panel-border:#d6d6d6;
  --dark:#3a3a3a;
  --tooltip:#333333;
  --blue:#4574b8;
  --blue-dark:#2f5a94;
  --link:#2d63b0;
  --text:#333333;
  --muted:#777777;
  --band:#f2f2f2;
  --avatar:#c8c8c8;
  --avatar-frame:#bdbdbd;
}
*{box-sizing:border-box;margin:0;padding:0}
html,body{width:1200px;height:951px;overflow:hidden}
body{position:relative;background:var(--page-bg);font-family:"Open Sans",Arial,sans-serif;color:var(--text);font-size:13px}
.abs{position:absolute}

/* header */
.site-header{left:0;top:0;width:1200px;height:108px;background:var(--header-bg);box-shadow:0 1px 3px rgba(0,0,0,.15)}
.brand{left:143px;top:22px;font-family:"PT Sans Narrow",Arial,sans-serif;font-weight:700;font-size:36px;color:#333;letter-spacing:-.3px}
.tag-search{left:397px;top:27px;width:467px;height:38px;background:#e2e2e2;border-radius:3px}
.tag-input{left:400px;top:30px;width:318px;height:33px;background:#fff;border:1px solid #d0d0d0;border-radius:2px;display:flex;align-items:center;padding-left:32px;color:#666;font-size:13.5px}
.tag-input svg{position:absolute;left:8px;top:8px}
.btn{background:var(--blue);color:#fff;border-radius:3px;display:flex;align-items:center;justify-content:center;font-size:13.5px;box-shadow:0 2px 0 var(--blue-dark)}
.btn-save{left:725px;top:30px;width:65px;height:32px}
.btn-clear{left:796px;top:30px;width:66px;height:32px}
.notify{left:923px;top:30px;width:38px;height:32px;background:#333;border-radius:3px}
.notify svg{position:absolute;left:10px;top:7px}
.tooltip{background:var(--tooltip);color:#fff;border-radius:2px;font-size:13.5px}
.tooltip::before{content:"";position:absolute;top:-6px;border:6px solid transparent;border-top:0;border-bottom-color:var(--tooltip)}
.tip-follower{left:893px;top:71px;width:108px;height:29px;display:flex;align-items:center;justify-content:center}
.tip-follower::before{left:48px}
.user-select{left:974px;top:30px;width:84px;height:32px;background:#fff;border:1px solid #d0d0d0;border-radius:3px;color:#aaa;font-size:13px;padding:7px 9px;overflow:hidden}
.user-select .caret{position:absolute;right:0;top:0;width:27px;height:32px;background:var(--blue)}
.user-select .caret svg{position:absolute;left:9px;top:13px}

/* sidebar */
.side-box{left:141px;width:234px;background:var(--panel-bg);border:1px solid var(--panel-border)}
.side-title{background:var(--dark);color:#fff;font-size:17px;height:38px;padding:7px 12px;margin:-1px -1px 0}
.side-search{margin:19px 9px 18px;height:32px;border:1px solid #ccc;border-radius:3px;color:#555;font-size:12.5px;padding:7px 9px;position:relative}
.side-search svg{position:absolute;right:10px;top:7px}
.side-list{list-style:none;padding:4px 0 6px}
.side-list li{height:29.5px;display:flex;align-items:center;padding-left:11px;font-size:12.5px;border-bottom:1px dashed #e2e2e2}
.side-list li:last-child{border-bottom:0}
.side-list li::before{content:"+";font-weight:600;width:16px;font-size:13px}
.show-all{background:var(--band);border-top:1px solid var(--panel-border);height:32px;padding:7px 11px;color:var(--link);font-size:12.5px}

/* main */
.breadcrumb{left:405px;top:128px;font-size:13.5px}
.breadcrumb a{color:var(--link);text-decoration:none}
.breadcrumb .sep{color:#555;margin:0 7px}
.tabs{left:403px;top:176px;height:38px;display:flex;border:1px solid #d0d0d0;background:#fff}
.tab{display:flex;align-items:center;justify-content:center;font-size:14px;border-right:1px solid #d0d0d0}
.tab:last-child{border-right:0}
.tab.active{background:var(--blue);color:#fff}
.tip-sort{left:394px;top:220px;width:108px;height:59px;padding:6px 17px;line-height:23.5px}
.tip-sort::before{left:48px}
.btn-create{left:941px;top:217px;width:117px;height:29px;font-size:13.5px}

.thread{left:403px;width:656px;background:var(--panel-bg);border:1px solid var(--panel-border)}
.thread-head{height:38px;background:var(--blue);color:#fff;font-size:13.5px;padding:9px 16px;margin:-1px -1px 0}
.avatar{position:absolute;background:var(--avatar);border:4px solid #fff;outline:2px solid var(--avatar-frame)}
.post{position:absolute;left:117px;width:524px;line-height:18.5px;font-size:13.5px}
.post p{margin-bottom:9.5px}
.post-meta{position:absolute;left:117px;width:524px;border-top:1px solid #d6d6d6;display:flex;align-items:center;font-size:13.5px}
.post-meta a{color:var(--link);margin-right:12px}
.post-meta .stat{margin-right:12px}
.actions{position:absolute;display:flex;gap:7px}
.actions .btn{height:29px;gap:8px;font-size:14px}
.reply-box{left:403px;top:494px;width:656px;height:98px;background:#fff;border:1px solid var(--panel-border)}
.reply-input{position:absolute;left:102px;top:11px;width:541px;height:71px;border:1px solid #ccc;padding:8px 15px;font-size:13.5px}
.tip-profile{left:394px;top:786px;width:112px;height:59px;padding:6px 12px;line-height:23.5px}
.tip-profile::before{left:50px}

.site-footer{left:0;top:904px;width:1200px;height:47px;background:var(--footer-bg);border-top:1px solid #b5b5b5}
</style>
</head>
<body>

<header class="site-header abs"></header>
<div class="brand abs">Company name</div>
<div class="tag-search abs"></div>
<div class="tag-input abs">
  <svg width="20" height="20" viewBox="0 0 20 20"><circle cx="8" cy="8" r="6" fill="none" stroke="#555" stroke-width="2"/><line x1="12.5" y1="12.5" x2="18" y2="18" stroke="#555" stroke-width="2.5"/></svg>
  #norvale #brightcap
</div>
<div class="btn btn-save abs">Save</div>
<div class="btn btn-clear abs">Clear</div>
<div class="notify abs"><svg width="18" height="18" viewBox="0 0 18 18"><circle cx="9" cy="5" r="4" fill="#fff"/><path d="M1 18v-3c0-3 3-5 8-5s8 2 8 5v3z" fill="#fff"/></svg></div>
<div class="tooltip tip-follower abs">1 new follower</div>
<div class="user-select abs">User<span class="caret"><svg width="10" height="7" viewBox="0 0 10 7"><path d="M0 0h10L5 7z" fill="#fff"/></svg></span></div>

<aside>
  <section class="side-box abs" style="top:128px;height:108px">
    <h2 class="side-title" style="font-weight:400">Users</h2>
    <div class="side-search">Search
      <svg width="20" height="20" viewBox="0 0 20 20"><circle cx="8" cy="8" r="6" fill="none" stroke="#555" stroke-width="2"/><line x1="12.5" y1="12.5" x2="18" y2="18" stroke="#555" stroke-width="2.5"/></svg>
    </div>
  </section>
  <section class="side-box abs" style="top:255px">
    <h2 class="side-title" style="font-weight:400">Saved filters</h2>
    <ul class="side-list"><li>Item One</li><li>Item Two</li><li>Item Three</li></ul>
    <div class="show-all">Show all</div>
  </section>
  <section class="side-box abs" style="top:446px">
    <h2 class="side-title" style="font-weight:400">Popular tage</h2>
    <ul class="side-list"><li>Item One</li><li>Item Two</li><li>Item Three</li></ul>
    <div class="show-all">Show all</div>
  </section>
  <section class="side-box abs" style="top:638px">
    <h2 class="side-title" style="font-weight:400">Popular contributors</h2>
    <ul class="side-list"><li>Item One</li><li>Item Two</li><li>Item Three</li></ul>
    <div class="show-all">Show all</div>
  </section>
</aside>

<nav class="breadcrumb abs"><a href="#">Home</a><span class="sep">»</span><a href="#">Conversations</a><span class="sep">»</span>Public #norvale#brightcap</nav>

<div class="tabs abs">
  <div class="tab active" style="width:77px">Public</div>
  <div class="tab" style="width:99px">Following</div>
  <div class="tab" style="width:88px">Contacts</div>
</div>
<div class="btn btn-create abs">Create thread</div>

<article class="thread abs" style="top:255px;height:230px">
  <div class="thread-head"></div>
  <div class="avatar" role="img" aria-label="Author profile picture" style="left:10px;top:48px;width:92px;height:92px"></div>
  <div class="post" style="top:47px">
    <p>Lorem ipsum dolor sit amet,</p>
    <p>Posted by Martin Hale on 01/01/2014 - 15:32</p>
    <p>Lorem ipsum dolor sit amet, consectetuer adipiscing elit, sed diam nonummy nibh euismod tincidunt ut laoreet dolore magna aliquam erat volutpat. Ut wisi enim ad minim veniam, quis nostrud exerci tation ullamcorper suscipit lobortis nisl ut aliquip ex ea commodo consequat.</p>
  </div>
  <div class="post-meta" style="top:186px;height:43px;padding-bottom:6px"><a href="#">Read more</a><span class="stat">12 replies</span><span class="stat">250 views</span></div>
  <div class="actions" style="left:372px;top:194px">
    <div class="btn" style="width:75px"><svg width="14" height="11" viewBox="0 0 14 11"><path d="M5 0L0 5l5 5V7c4 0 7 1 9 4 0-5-3-8-9-8z" fill="#fff"/></svg>Reply</div>
    <div class="btn" style="width:79px"><svg width="14" height="14" viewBox="0 0 14 14"><circle cx="11" cy="2.5" r="2.3" fill="#fff"/><circle cx="3" cy="7" r="2.3" fill="#fff"/><circle cx="11" cy="11.5" r="2.3" fill="#fff"/><path d="M11 2.5L3 7l8 4.5" stroke="#fff" stroke-width="1.4" fill="none"/></svg>Share</div>
    <div class="btn" style="width:103px"><svg width="16" height="15" viewBox="0 0 16 15"><path d="M8 0l2.4 5 5.6.6-4.2 3.8 1.2 5.6L8 12.1 3 15l1.2-5.6L0 5.6 5.6 5z" fill="#fff"/></svg>Favourite</div>
  </div>
</article>
<div class="tooltip tip-sort abs">Recent<br>Popular</div>

<section class="reply-box abs">
  <div class="avatar" role="img" aria-label="Your profile picture" style="left:11px;top:11px;width:73px;height:73px"></div>
  <div class="reply-input">type your reply here</div>
</section>

<article class="thread abs" style="top:639px;height:230px">
  <div class="thread-head">Thead #2</div>
  <div class="avatar" role="img" aria-label="Author profile picture" style="left:10px;top:49px;width:92px;height:92px"></div>
  <div class="post" style="top:48px">
    <p>Lorem ipsum dolor sit amet,</p>
    <p>Posted by Martin Hale on 01/01/2014 - 15:32</p>
    <p>Lorem ipsum dolor sit amet, consectetuer adipiscing elit, sed diam nonummy nibh euismod tincidunt ut laoreet dolore magna aliquam erat volutpat. Ut wisi enim ad minim veniam, quis nostrud exerci tation ullamcorper suscipit lobortis nisl ut aliquip ex ea commodo consequat.</p>
  </div>
  <div class="post-meta" style="top:187px;height:43px;padding-bottom:6px"><a href="#">Read more</a><span class="stat">12 replies</span><span class="stat">250 views</span></div>
  <div class="actions" style="left:372px;top:195px">
    <div class="btn" style="width:75px"><svg width="14" height="11" viewBox="0 0 14 11"><path d="M5 0L0 5l5 5V7c4 0 7 1 9 4 0-5-3-8-9-8z" fill="#fff"/></svg>Reply</div>
    <div class="btn" style="width:79px"><svg width="14" height="14" viewBox="0 0 14 14"><circle cx="11" cy="2.5" r="2.3" fill="#fff"/><circle cx="3" cy="7" r="2.3" fill="#fff"/><circle cx="11" cy="11.5" r="2.3" fill="#fff"/><path d="M11 2.5L3 7l8 4.5" stroke="#fff" stroke-width="1.4" fill="none"/></svg>Share</div>
    <div class="btn" style="width:103px"><svg width="16" height="15" viewBox="0 0 16 15"><path d="M8 0l2.4 5 5.6.6-4.2 3.8 1.2 5.6L8 12.1 3 15l1.2-5.6L0 5.6 5.6 5z" fill="#fff"/></svg>Favourite</div>
  </div>
</article>
<div class="tooltip tip-profile abs">View profile<br>View all posts</div>

<footer class="site-footer abs"></footer>

</body>
</html>
```